Business Card Admin Services

I have just selected a new logo. Now I need a business card.

The business is contract administrative services. We provide high value administrative services to small businesses/offices. We are professional, efficient, but also have fun and energetic personalities.

Olive Parker
Olive@OfficeFalcon.ca
604-319-4870
OfficeFalcon.ca

I will also want Facebook, Twitter and LinkedIn icons on the card - please up my "handles" beside each.
Facebook is OfficeFalconCanada
Twitter is @OFalconOlive
LinkedIn is OliveParkerOfficeFalcon
Updates

New logo just updated.  Thanks for your patience!

Target Market(s)

Small businesses, professional offices

Industry/Entity Type

Business

Requirements
Must have
• bold, fun use of my colours
font needs to be consistent with the logo
Nice to have
• I quite like a closeup of the head

```html
<!DOCTYPE html>
<html lang="en">
<head>
<meta charset="utf-8">
<title>Office Falcon – Business Card</title>
<link rel="stylesheet" href="https://fonts.googleapis.com/css2?family=Montserrat:wght@300;400;600;700&family=Open+Sans:wght@400;600;700&display=swap">
<style>
  :root {
    --stage: #2a2a2a;
    --card: #ececec;
    --head-grey: #cdcdcd;
    --pink: #e6137e;
    --ink: #1e1e1e;
    --icon: #222222;
  }
  * { box-sizing: border-box; margin: 0; padding: 0; }
  html, body { width: 1200px; height: 900px; overflow: hidden; }
  body {
    background: var(--stage);
    display: flex;
    flex-direction: column;
    align-items: center;
    justify-content: center;
    gap: 36px;
    font-family: "Open Sans", Arial, sans-serif;
  }
  .card {
    position: relative;
    width: 700px;
    height: 400px;
    background: var(--card);
    overflow: hidden;
    box-shadow: 0 10px 30px rgba(0,0,0,.45);
  }
  .head-closeup {
    position: absolute;
    width: 520px;
    height: 520px;
    border-radius: 50%;
    background: var(--head-grey);
  }
  .card--front .head-closeup { right: -210px; top: -250px; }
  .card--back .head-closeup { right: -250px; top: -150px; }

  .brand {
    position: absolute;
    display: flex;
    align-items: center;
    gap: 16px;
  }
  .brand__mark {
    border-radius: 50%;
    background: var(--pink);
    flex: none;
  }
  .brand__name {
    font-family: "Montserrat", Arial, sans-serif;
    font-weight: 600;
    color: var(--pink);
    text-transform: uppercase;
    letter-spacing: 1px;
    white-space: nowrap;
  }
  .card--front .brand { left: 70px; top: 160px; }
  .card--front .brand__mark { width: 110px; height: 110px; }
  .card--front .brand__name { font-size: 44px; }

  .card--back .brand { left: 60px; top: 46px; }
  .card--back .brand__mark { width: 62px; height: 62px; }
  .card--back .brand__name { font-size: 36px; }

  .contact {
    position: absolute;
    left: 62px;
    top: 200px;
    color: var(--ink);
  }
  .contact__name {
    font-family: "Montserrat", Arial, sans-serif;
    font-size: 20px;
    font-weight: 400;
    letter-spacing: 2px;
    text-transform: uppercase;
    margin-bottom: 28px;
  }
  .contact__name strong { color: var(--pink); font-weight: 700; }
  .contact__list { list-style: none; font-size: 18px; line-height: 1.55; }
  .contact__label { color: var(--pink); font-weight: 700; }

  .social {
    position: absolute;
    right: 48px;
    top: 228px;
    text-align: left;
  }
  .social__title {
    font-size: 13px;
    color: var(--pink);
    text-transform: uppercase;
    letter-spacing: .5px;
    margin-bottom: 10px;
  }
  .social__icons { display: flex; gap: 18px; }
  .social__icon {
    width: 24px;
    height: 24px;
    border-radius: 3px;
    background: var(--icon);
  }
</style>
</head>
<body>

  <section class="card card--front" aria-label="Business card front">
    <div class="head-closeup" role="img" aria-label="Large close-up of the brand mascot's head"></div>
    <div class="brand">
      <span class="brand__mark"></span>
      <span class="brand__name">Office Falcon</span>
    </div>
  </section>

  <section class="card card--back" aria-label="Business card back">
    <div class="head-closeup" role="img" aria-label="Large close-up of the brand mascot's head"></div>
    <div class="brand">
      <span class="brand__mark"></span>
      <span class="brand__name">Office Falcon</span>
    </div>

    <div class="contact">
      <p class="contact__name">Olive <strong>Parker</strong></p>
      <ul class="contact__list">
        <li><span class="contact__label">Tel:</span> 604-319-4870</li>
        <li><span class="contact__label">Email:</span> Olive@OfficeFalcon.ca</li>
        <li><span class="contact__label">Web:</span> OfficeFalcon.ca</li>
      </ul>
    </div>

    <div class="social">
      <p class="social__title">Follow us on</p>
      <div class="social__icons">
        <span class="social__icon" role="img" aria-label="Social network icon"></span>
        <span class="social__icon" role="img" aria-label="Social network icon"></span>
        <span class="social__icon" role="img" aria-label="Social network icon"></span>
      </div>
    </div>
  </section>

</body>
</html>
```